RW Demolition business cards v.2 first was me

So the ones in the picture are my original cards that I came up with. 😅however I kinda messed up on two things, I missed spelled my name it should be Leandro Vasquez as well as the email should be Leandrov@bluepeakworks.com. I would like to clean this card up and also make it pop! Something that people would remember me by and that screams DEMOLITION. As well as a card that give you a feeling of loyalty and trust. I would also like to change and remove junk hauling and add full demolition to replace it. These cards worked for a little while but I cant make that my image while handing these out. I would also like to only put down that we are located in Laguna Crest Valley, CA, 92601 instead of the address on the card. Also if we can have a line that states Licensed, Bonded, & Insured. With out License # 4837251

Target Market(s)

Contractors and Home owners

Industry/Entity Type

Construction specialist in Demolition

Contact Information for Business Card

R Demolition Selective Demolition & Full Demolition Kitchens AD Preparation Bathrooms Sheds Interiors & Exteriors Demo Digging And Much More Leandrro Vasquez Owner our city state and zip

Font styles to use
Serif
Sans Serif
Decorative

Colors
0054AA
0677BA
7BADD7
CADEEF
E8F1F8
0094D4
00A9DD
6FCCEA
C7EBF8
E9F6FB

Requirements
Must have
• License# 4837251
Nice to have
• Trying to go with a blue and white color scheme
Should not have
• Building construction

```html
<!DOCTYPE html>
<html lang="en">
<head>
<meta charset="utf-8">
<title>RW Demolition Business Cards</title>
<link href="https://fonts.googleapis.com/css2?family=Cinzel:wght@500&family=Montserrat:wght@400;500;600;700&display=swap" rel="stylesheet">
<style>
  :root {
    --backdrop: #bdbdbd;
    --card-white: #ffffff;
    --brand-blue: #0f4f9a;
    --ink: #1c1c1c;
    --muted: #3a3a3a;
    --rule: #555555;
    --on-blue: #ffffff;
    --rule-on-blue: #7badd7;
  }
  * { box-sizing: border-box; margin: 0; padding: 0; }
  html, body { width: 1200px; height: 802px; overflow: hidden; }
  body {
    background: linear-gradient(180deg, #cfcfcf, var(--backdrop));
    font-family: "Montserrat", sans-serif;
    display: flex; align-items: center; justify-content: center; gap: 40px;
  }
  .card {
    width: 540px; height: 309px; border-radius: 24px; position: relative;
    box-shadow: 0 14px 30px rgba(0,0,0,.3);
    overflow: hidden;
  }
  /* front */
  .card-front { background: var(--card-white); color: var(--ink); }
  .brand { position: absolute; text-align: right; }
  .card-front .brand { top: 40px; right: 70px; }
  .brand-name {
    display: flex; align-items: center; gap: 10px;
    font-weight: 700; font-size: 30px; letter-spacing: .5px; text-transform: uppercase;
  }
  .brand-dot { width: 14px; height: 14px; border-radius: 50%; background: currentColor; }
  .card-front .brand-name { color: var(--brand-blue); }
  .brand-license { font-size: 9px; font-weight: 600; letter-spacing: 1px; margin-top: 2px; }
  .address {
    position: absolute; right: 40px; top: 140px; text-align: right;
    font-size: 12px; line-height: 1.4; color: var(--muted);
  }
  .person { position: absolute; left: 40px; top: 170px; }
  .person-name { font-family: "Cinzel", serif; font-size: 21px; color: var(--brand-blue); }
  .person-role { font-size: 12px; color: var(--muted); }
  .divider { position: absolute; left: 40px; right: 40px; top: 222px; border-top: 1px solid var(--rule); }
  .contacts { position: absolute; left: 40px; top: 232px; list-style: none; font-size: 12px; line-height: 1.55; color: var(--ink); }
  .contacts li { display: flex; align-items: center; gap: 8px; }
  .contacts svg { width: 11px; height: 11px; fill: var(--brand-blue); }
  /* back */
  .card-back { background: var(--brand-blue); color: var(--on-blue); text-align: center; }
  .card-back .brand { position: static; display: inline-block; margin-top: 52px; }
  .card-back .brand-name { font-size: 34px; }
  .services-title { font-size: 22px; font-weight: 600; margin-top: 14px; }
  .services-sub { font-size: 13px; margin-top: 2px; }
  .services-rule { width: 260px; margin: 8px auto 10px; border-top: 1px solid var(--rule-on-blue); }
  .services { font-size: 13px; line-height: 1.7; }
</style>
</head>
<body>
  <section class="card card-front">
    <div class="brand">
      <div class="brand-name"><span class="brand-dot"></span>RW Demolition</div>
      <div class="brand-license">LICENSE#4837251</div>
    </div>
    <div class="address">Laguna Crest Valley<br>CA, 92601</div>
    <div class="person">
      <div class="person-name">Leandro Vasquez</div>
      <div class="person-role">Owner</div>
    </div>
    <div class="divider"></div>
    <ul class="contacts">
      <li><svg viewBox="0 0 24 24"><path d="M6.6 10.8a15.1 15.1 0 0 0 6.6 6.6l2.2-2.2c.3-.3.7-.4 1-.2 1.1.4 2.3.6 3.6.6.6 0 1 .4 1 1V20c0 .6-.4 1-1 1C10.6 21 3 13.4 3 4c0-.6.4-1 1-1h3.5c.6 0 1 .4 1 1 0 1.3.2 2.5.6 3.6.1.3 0 .7-.2 1z"/></svg>(555)310-4872</li>
      <li><svg viewBox="0 0 24 24"><path d="M2 5h20v14H2zm2 2v.5l8 5 8-5V7l-8 5z"/></svg>Leandrov@bluepeakworks.com</li>
      <li><svg viewBox="0 0 24 24"><circle cx="12" cy="12" r="10"/></svg>www.bluepeakworks.com</li>
    </ul>
  </section>

  <section class="card card-back">
    <div class="brand">
      <div class="brand-name"><span class="brand-dot"></span>RW Demolition</div>
      <div class="brand-license">LICENSE#4837251</div>
    </div>
    <h2 class="services-title">R Demolition</h2>
    <p class="services-sub">Selective Demolition &amp; Full Demolition</p>
    <div class="services-rule"></div>
    <p class="services">Kitchens &bull; AD Preparation &bull; Bathrooms &bull; Sheds<br>Interiors &amp; Exteriors Demo &bull; Digging &bull; And Much More</p>
  </section>
</body>
</html>
```